Graphic to show our studio's values

We'd like to create a graphic of our values that can go onto fun gifts for our team in order to keep our values in front of all of us in a creative way. The graphic might go onto mugs, gift boxes, tote bags, etc. We are a growing interior architecture/design studio in Austin, TX. I encourage you to check out our website at www.vorrelandesign.com to get a sense of our vibe and culture. The graphic may or may not include the subtext to each value depending on how difficult it is to incorporate the subtext into a great design.

```html
<!DOCTYPE html>
<html lang="en">
<head>
<meta charset="utf-8">
<title>Vorrelan Design – Our Values</title>
<link rel="stylesheet" href="https://fonts.googleapis.com/css2?family=Oswald:wght@300;400;500&display=swap">
<style>
  :root {
    --pill: #616265;
    --accent: #b4cf3c;
    --ink-light: #ffffff;
    --bg-center: #ffffff;
    --bg-edge: #c8c8c8;
  }
  html, body { margin: 0; padding: 0; overflow: hidden; }
  .canvas {
    position: relative;
    width: 1200px;
    height: 824px;
    overflow: hidden;
    background: radial-gradient(ellipse at 50% 50%, var(--bg-center) 0%, #ececec 45%, var(--bg-edge) 100%);
    font-family: "Oswald", "Arial Narrow", sans-serif;
  }
  .graphics { position: absolute; left: 0; top: 0; }
  .wordmark {
    position: absolute;
    left: 0; width: 1200px; top: 122px;
    margin: 0;
    text-align: center;
    color: var(--pill);
    font-weight: 500;
    font-size: 40px;
    line-height: 1;
  }
  .value { position: absolute; color: var(--ink-light); }
  .value-title {
    margin: 0;
    font-weight: 500;
    font-size: 50px;
    line-height: 1;
    letter-spacing: -0.6px;
  }
  .value-text {
    margin: 5px 0 0 0;
    font-weight: 300;
    font-size: 14.2px;
    line-height: 16px;
  }
  .value--learners { left: 469px; top: 246px; }
  .value--learners .value-text { margin-left: -14px; }
  .value--responsive { left: 187px; top: 412px; }
  .value--responsive .value-text { margin-left: 5px; }
  .value--trustworthy { left: 746px; top: 412px; }
  .value--trustworthy .value-text { margin-left: 4px; }
  .value--positive { left: 496px; top: 595px; }
  .value--positive .value-text { margin-left: 6px; margin-top: 7px; }
</style>
</head>
<body>
<div class="canvas">
  <svg class="graphics" width="1200" height="824" viewBox="0 0 1200 824" aria-hidden="true">
    <g fill="none" stroke="var(--accent)" stroke-width="8">
      <path d="M420 347 A216 216 0 0 0 397 400"/>
      <path d="M396 513 A216 216 0 0 0 425 578"/>
      <path d="M790 347 A216 216 0 0 1 813 400"/>
      <path d="M814 513 A216 216 0 0 1 785 578"/>
    </g>
    <g stroke="var(--accent)" stroke-width="4" fill="none">
      <line x1="605" y1="347" x2="605" y2="575"/>
      <line x1="570" y1="459" x2="638" y2="459"/>
      <circle cx="605" cy="459" r="17" fill="var(--pill)" stroke-width="6"/>
    </g>

    <g fill="var(--pill)">
      <rect class="pill" x="358" y="240" width="491" height="99" rx="49.5"/>
      <rect class="pill" x="71" y="407" width="492" height="98" rx="49"/>
      <rect class="pill" x="644" y="407" width="492" height="98" rx="49"/>
      <rect class="pill" x="388" y="584" width="431" height="98" rx="49"/>
    </g>

    <g class="icon-bulb" fill="#fff" stroke="#fff">
      <g stroke-width="2.5" stroke-linecap="round">
        <line x1="411" y1="254" x2="411" y2="266"/>
        <line x1="389" y1="263" x2="397" y2="271"/>
        <line x1="433" y1="263" x2="425" y2="271"/>
        <line x1="377" y1="286" x2="389" y2="286"/>
        <line x1="433" y1="286" x2="445" y2="286"/>
      </g>
      <path stroke="none" d="M411 272 a15 15 0 0 1 9 27 c-2 2 -3 4 -3 7 h-12 c0 -3 -1 -5 -3 -7 a15 15 0 0 1 9 -27z"/>
      <rect stroke="none" x="404" y="308" width="14" height="2.5" rx="1"/>
      <rect stroke="none" x="404" y="312" width="14" height="2.5" rx="1"/>
      <rect stroke="none" x="406" y="316" width="10" height="2.5" rx="1"/>
    </g>

    <g class="icon-reply">
      <g transform="rotate(-8 145 456)">
        <rect x="118" y="438" width="54" height="36" fill="#fff"/>
        <path d="M119 439 L145 460 L171 439" fill="none" stroke="var(--pill)" stroke-width="2.5"/>
        <path d="M119 473 L138 455 M171 473 L152 455" fill="none" stroke="var(--pill)" stroke-width="2"/>
      </g>
      <path fill="#fff" stroke="var(--pill)" stroke-width="2" d="M88 466 L113 446 L113 457 C130 456 144 466 146 490 C138 478 128 474 113 475 L113 486 Z"/>
    </g>

    <g class="icon-shield" fill="none" stroke="#fff">
      <path stroke-width="6" d="M700 425 C689 432 680 434 673 434 C673 458 678 476 700 487 C722 476 727 458 727 434 C720 434 711 432 700 425Z"/>
      <path stroke="none" fill="#fff" d="M683 455 L691 449 L700 460 L732 428 L737 433 L700 471 Z"/>
    </g>

    <g class="icon-thumb">
      <path fill="#fff" d="M431 596 C438 596 442 604 440 615 L438 620 L462 620 C467 620 468 625 466 627 L466 651 C466 656 462 658 456 658 L425 658 L420 655 L420 622 C426 616 430 608 431 596Z"/>
      <rect x="464" y="624" width="10" height="34" rx="2" fill="#fff"/>
      <ellipse cx="415" cy="628" rx="6" ry="5" fill="#fff"/>
      <ellipse cx="414" cy="639" rx="6" ry="5" fill="#fff"/>
      <ellipse cx="415" cy="650" rx="6" ry="5" fill="#fff"/>
      <g stroke="var(--pill)" stroke-width="5">
        <line x1="443" y1="627" x2="443" y2="652"/>
        <line x1="431" y1="639" x2="456" y2="639"/>
      </g>
    </g>
  </svg>

  <p class="wordmark">Vorrelan Design</p>

  <section class="value value--learners">
    <h2 class="value-title">We are Learners</h2>
    <p class="value-text">We respond to our cleints quickly &amp; with enthusiasm as engaged teamamtes<br>who are committed to partnering with them in accomplishing their goals</p>
  </section>

  <section class="value value--responsive">
    <h2 class="value-title">We are Responsive</h2>
    <p class="value-text">We look for opportunity to learn from every project and interaction,<br>and we share what we learn from each other.</p>
  </section>

  <section class="value value--trustworthy">
    <h2 class="value-title">We are Trustworthy</h2>
    <p class="value-text">We look for the good, roll with the punches, have a sense of humour<br>and celebrate each other</p>
  </section>

  <section class="value value--positive">
    <h2 class="value-title">We are Positive</h2>
    <p class="value-text">We are our client’s advocate and trustworthy teammate.</p>
  </section>
</div>
</body>
</html>
```